Democracy in crisis book

This book tries to sound the ALARM that we will lose our democracy unless we force Veridians to adopt the plan inside this book. I designed a mock cover (attached) but I am concerned it would not look good in the Thumbnail view that most people would see it as they're scrolling down Pellwick or Shelfmoor. The final title for the book is: Final Hour to Rescue the Shared Republic. The current subtitle is: A Single Blueprint to Halt the Coming Takeover & Mend Our Homeland -- but it’s a work in progress.The subtitle is still working progress but it's really not that important and can be small.
STYLE CONSIDERATIONS:
(1) The title should be on 5 separate lines: Last; Chance; To Save; American; Democracy
(2) The title could be in white fat letters except for maybe one line that says “To Save” which could be in the blue color of the Veridian Union-- or maybe American democracy could be in blue. We may have to try a few variations of that.
(3) I picked the red in the mock cover to connotate an emergency,
(4) I liked big bold fat font going across the full page so that it looks like a major warning sign, though note I was unable to extend each line flush all the way to the right which I think would have been better.
(5) I liked it better flush to left instead of centered.
(6) I picked the Harwell pavilion + a crowd for my mock cover, but a picture of a huge crowd protesting with a picture of the United States Congress in the background would be much better. DO NOT USE HARWELL. Obviously I would need it to be an open license or something I can pay a small amount to get. If you can find that picture then the page should probably be colored in red with Congress in white.
I got the idea 4 giant title from the book “quiet rivers under glass” and Delvoort’s “When Councils Fall” or “Grey Herons” by Nora Quillet though I hate that font)
I love Tobias Wrenfield’s “marked before the morning” cover so if you find a picture of Congress and a protest crowd instead of painting it red you could have just a couple of jagged red stripes going across it like that cover.
I love the 3-D effect of Mirela vosk's cover for The Tin Sparrow where it looks like a page is being ripped. That effect could be done the words American democracy like it's being torn off the page UPDATE: MANY DESIGNERS TRIED THAT & IT DID NOT WORK AT ALL.
Note that this book will be submitted to many award competitions, so please give me an award-winning cover.
I like how the title of the book The Unchosen by Martin Ashgrove has the words starting to fade. I don't like the ladder on it, but maybe 'American democracy' could fade like that.
Veridians

```html
<!DOCTYPE html>
<html lang="en">
<head>
<meta charset="utf-8">
<title>Final Hour to Rescue the Shared Republic — Book Cover</title>
<link rel="stylesheet" href="https://fonts.googleapis.com/css2?family=Anton&family=Oswald:wght@300;500&display=swap">
<style>
  :root {
    --ink: #141414;
    --ink-soft: #222;
    --alarm-red: #7c1417;
    --union-blue: #3f7cc4;
    --marble-light: #f1efec;
    --marble-mid: #cfcbc6;
    --marble-dark: #9d9893;
    --paper: #ffffff;
  }
  html, body {
    margin: 0;
    padding: 0;
    width: 851px;
    height: 1200px;
    overflow: hidden;
    background: var(--ink);
  }
  .cover {
    position: relative;
    width: 851px;
    height: 1200px;
    overflow: hidden;
    background: radial-gradient(ellipse at 40% 35%, var(--ink-soft) 0%, var(--ink) 70%);
  }
  .crowd-art {
    position: absolute;
    left: 0;
    bottom: 0;
    width: 851px;
    height: 330px;
    background: linear-gradient(180deg, rgba(20,20,20,0) 0%, var(--marble-dark) 22%, var(--marble-mid) 55%, var(--marble-light) 100%);
  }
  .title-block, .author {
    position: absolute;
    left: 0;
    top: 0;
  }
  .title-line {
    font-family: "Anton", "Oswald", sans-serif;
    text-transform: uppercase;
  }
  .title-line--alarm { fill: var(--alarm-red); }
  .title-line--marble { fill: url(#marbleFill); }
  .title-line--blue { fill: var(--union-blue); }
  .title-line--fading { fill: url(#fadeFill); }
  .author-name {
    font-family: "Oswald", sans-serif;
    font-weight: 300;
    fill: var(--paper);
  }
  .subtitle-band {
    position: absolute;
    left: 56px;
    top: 1044px;
    width: 772px;
    height: 92px;
  }
  .subtitle-band svg { position: absolute; inset: 0; }
  .subtitle {
    position: absolute;
    left: 8px;
    top: 14px;
    margin: 0;
    font-family: "Oswald", sans-serif;
    font-weight: 500;
    font-size: 27px;
    line-height: 36px;
    color: var(--paper);
  }
</style>
</head>
<body>
<main class="cover">
  <div class="crowd-art" role="img" aria-label="Pale marble-toned crowd of raised arms and protesters in silhouette rising from the bottom of the cover"></div>

  <svg class="title-block" width="851" height="880" viewBox="0 0 851 880" aria-label="Final Hour to Rescue the Shared Republic">
    <defs>
      <linearGradient id="marbleFill" x1="0" y1="0" x2="1" y2="1">
        <stop offset="0" stop-color="#f4f2ef"/>
        <stop offset="0.5" stop-color="#d9d5d0"/>
        <stop offset="1" stop-color="#b9b4ae"/>
      </linearGradient>
      <linearGradient id="fadeFill" x1="0" y1="0" x2="1" y2="1">
        <stop offset="0" stop-color="#e8e5e1" stop-opacity="0.9"/>
        <stop offset="1" stop-color="#a9a49e" stop-opacity="0.7"/>
      </linearGradient>
    </defs>
    <text class="title-line title-line--alarm" x="62" y="340" font-size="322" textLength="606" lengthAdjust="spacingAndGlyphs">Final</text>
    <text class="title-line title-line--marble" x="52" y="512" font-size="184" textLength="580" lengthAdjust="spacingAndGlyphs">Hour</text>
    <text class="title-line title-line--blue" x="92" y="604" font-size="97" textLength="540" lengthAdjust="spacingAndGlyphs">To Rescue the</text>
    <text class="title-line title-line--marble" x="52" y="740" font-size="147" textLength="588" lengthAdjust="spacingAndGlyphs">Shared</text>
    <text class="title-line title-line--fading" x="56" y="856" font-size="124" textLength="576" lengthAdjust="spacingAndGlyphs">Republic</text>
  </svg>

  <svg class="author" width="851" height="880" viewBox="0 0 851 880" aria-label="Hollis Dane McKerrow">
    <text class="author-name" x="60" y="-756" font-size="32" transform="rotate(90)" textLength="796" lengthAdjust="spacing">HOLLIS DANE MCKERROW</text>
  </svg>

  <div class="subtitle-band">
    <svg width="772" height="92" viewBox="0 0 772 92" aria-hidden="true">
      <path d="M0 6 L690 0 L772 8 L760 40 L700 62 L600 74 L540 92 L0 90 Z" fill="var(--alarm-red)"/>
    </svg>
    <p class="subtitle">A Single Blueprint to Halt the Coming<br>Takeover &amp; Mend Our Homeland</p>
  </div>
</main>
</body>
</html>
```